Quirky Coffee Shop Loyalty Card

We need a new loyalty card in business card size format for our independent coffee shop. We are a quirky, ethically focussed, high quality coffee establishment with a focus on cutting edge products like siphon coffee and flamed latte brules. Projecting an image of high quality, innovation, ethical and eco-friendly with a quirky and unique feel. We would like a green background appearance, echoing or complementing the green in our logo (uploaded). Our coffee is organic and ethically sourced, we would like to communicate this - it doesn't need to be done in obvious way, open to creative suggestions. Earthy and straightforward in approach is important to us. We use cups made from 100% repurposed coffee husk, called Pellora (https://pellora.example/). One idea we had would be to have this cup image on the card with arrows pointing in from words like "Organic", "Made from coffee husks", "Ethical" etc... but in a less cliche'd way than this sounds!Please note that although this is a business card size, we need a loyalty card not a business card. On the back, we need to convey that the customer buys 8 coffees and gets the ninth free. We also need our social media links, email and address:
FB: @tinymugworksfendle
Insta: Tinymugworks
Email: fendle@tinymugworks.example
Address: No.4 Marrow Lane, ZZ9 4XJ
Phone: 01999 456018

Target Market(s)

All shop customers

Industry/Entity Type

Coffee Shop

Contact Information for Business Card

FB: @tinymugworksfendle
Insta: Tinymugworks
Phone: 01999 456018

Colors

Designer to choose colors to be used in the design.

Requirements
Must have
• Quirky, ethical, organic feel
Should not have
• Well-used or obvious coffee shop imagery

```html
<!DOCTYPE html>
<html lang="en">
<head>
<meta charset="utf-8">
<title>Tinymugworks Loyalty Card</title>
<link rel="stylesheet" href="https://fonts.googleapis.com/css2?family=Jura:wght@500&family=Roboto:wght@500&family=Work+Sans:wght@400&display=swap">
<style>
  :root {
    --page: #e9e4dc;
    --brown: #8b4c14;
    --brown-dark: #6a3511;
    --green: #6dbe45;
    --white: #ffffff;
    --grey-text: #5a5a5a;
    --husk-light: #f6f3ef;
  }
  * { margin: 0; padding: 0; box-sizing: border-box; }
  html, body { width: 1200px; height: 900px; overflow: hidden; }
  body { background: var(--page); position: relative; font-family: "Roboto", sans-serif; }

  .card {
    position: absolute; left: 261px; width: 656px; height: 358px;
    border-radius: 24px; overflow: hidden;
    box-shadow: 0 4px 14px rgba(0,0,0,.18);
  }
  .card--front { top: 69px; background: var(--white); }
  .card--back { top: 472px; background: var(--brown); }

  /* front */
  .bean-field {
    position: absolute; left: 0; top: 0; width: 375px; height: 100%;
    background: radial-gradient(circle at 50% 50%, var(--white), var(--husk-light));
  }
  .drink-photo {
    position: absolute; left: 375px; top: 0; width: 281px; height: 100%;
    background: linear-gradient(160deg, #3b3a3c 0%, #6b4a2f 40%, #b06a36 65%, #7a4a25 100%);
  }
  .brand-seal {
    position: absolute; left: 27px; top: 91px; width: 174px; height: 174px;
    border: 6px solid var(--brown); border-radius: 50%;
    display: flex; align-items: center; justify-content: center;
    background: var(--white);
  }
  .brand-name { color: var(--green); font-family: "Roboto", sans-serif; font-weight: 500; font-size: 22px; }
  .pointer { position: absolute; left: 210px; top: 138px; }
  .husk-claim {
    position: absolute; left: 27px; top: 316px;
    font-family: "Roboto", sans-serif; font-weight: 500; font-size: 20px;
    color: var(--brown); letter-spacing: .2px;
  }

  /* back */
  .offer {
    position: absolute; left: 35px; top: 18px;
    font-family: "Jura", sans-serif; font-weight: 500; font-size: 31px;
    color: var(--white); letter-spacing: .5px; white-space: nowrap;
  }
  .stamp {
    position: absolute; width: 68px; height: 68px; border-radius: 50%;
    background: var(--white); border: 3px solid var(--green);
    display: flex; align-items: center; justify-content: center;
    font-family: "Roboto", sans-serif; font-weight: 500; font-size: 34px; color: var(--brown);
  }
  .address-band { position: absolute; left: 0; top: 260px; width: 100%; height: 27px; background: var(--white); }
  .contact-band { position: absolute; left: 0; top: 287px; width: 100%; height: 71px; background: var(--green); }
  .contact-band-rise { position: absolute; left: 560px; top: 275px; width: 96px; height: 20px; background: var(--green); }

  .free-reward-art {
    position: absolute; left: 451px; top: 82px; width: 159px; height: 210px;
    border-radius: 6px;
    background: linear-gradient(180deg, var(--brown-dark) 0%, #5e2f10 100%);
  }
  .free-label {
    position: absolute; left: 451px; top: 174px; width: 159px;
    text-align: center; line-height: 40px;
    font-family: "Roboto", sans-serif; font-weight: 500; font-size: 33px; color: var(--white);
  }

  .contact {
    position: absolute; display: flex; align-items: center; gap: 9px;
    font-family: "Work Sans", sans-serif; font-size: 16px; color: var(--white); white-space: nowrap;
  }
  .contact--address { color: var(--grey-text); top: 264px; left: 33px; }
  .contact svg { flex: none; }
  .dot-mark { width: 9px; height: 9px; background: var(--white); flex: none; }
  .dot-mark--round { border-radius: 50%; }
</style>
</head>
<body>

<section class="card card--front">
  <div class="bean-field" role="img" aria-label="Faint scattered coffee bean pattern"></div>
  <div class="drink-photo" role="img" aria-label="Photo of a copper pot of spiced coffee with a cinnamon stick on a wooden tray"></div>
  <div class="brand-seal"><span class="brand-name">Tinymugworks</span></div>
  <svg class="pointer" width="156" height="84" viewBox="0 0 156 84" aria-hidden="true">
    <rect x="0" y="36" width="144" height="11" fill="var(--green)"/>
    <polygon points="113,0 156,42 113,84 113,66 138,42 113,18" fill="var(--green)"/>
  </svg>
  <p class="husk-claim">MADE FROM COFFEE HUSKS</p>
</section>

<section class="card card--back">
  <h1 class="offer">Buys 8 coffees and gets the one free.</h1>

  <div class="stamp" style="left:35px;top:81px">1</div>
  <div class="stamp" style="left:142px;top:81px">2</div>
  <div class="stamp" style="left:249px;top:81px">3</div>
  <div class="stamp" style="left:357px;top:81px">4</div>
  <div class="stamp" style="left:35px;top:172px">5</div>
  <div class="stamp" style="left:142px;top:172px">6</div>
  <div class="stamp" style="left:249px;top:172px">7</div>
  <div class="stamp" style="left:357px;top:172px">8</div>

  <div class="address-band"></div>
  <div class="contact-band-rise"></div>
  <div class="contact-band"></div>

  <div class="free-reward-art" role="img" aria-label="Illustration of a takeaway cup with a green lid and sleeve for the free ninth coffee"></div>
  <p class="free-label">FREE</p>

  <p class="contact contact--address">
    <svg width="10" height="14" viewBox="0 0 10 14" aria-hidden="true"><path d="M5 0a5 5 0 0 0-5 5c0 4 5 9 5 9s5-5 5-9a5 5 0 0 0-5-5zm0 7a2 2 0 1 1 0-4 2 2 0 0 1 0 4z" fill="var(--brown)"/></svg>
    No.4 Marrow Lane, ZZ9 4XJ
  </p>
  <p class="contact" style="left:35px;top:301px">
    <svg width="10" height="12" viewBox="0 0 10 12" aria-hidden="true"><path d="M2 0l2 3-1 1.5c.6 1.6 1.7 2.8 3 3.5L7.5 7 10 9l-1.5 2.5C4 11 1 6 .5 1.5z" fill="var(--white)"/></svg>
    01999 456018
  </p>
  <p class="contact" style="left:37px;top:323px">
    <span class="dot-mark dot-mark--round"></span>
    @tinymugworksfendle
  </p>
  <p class="contact" style="left:253px;top:301px">
    <span class="dot-mark"></span>
    Tinymugworks
  </p>
  <p class="contact" style="left:252px;top:323px">
    <svg width="11" height="8" viewBox="0 0 11 8" aria-hidden="true"><rect x=".6" y=".6" width="9.8" height="6.8" fill="none" stroke="var(--white)" stroke-width="1.2"/><path d="M.6.6l4.9 3.8L10.4.6" fill="none" stroke="var(--white)" stroke-width="1.2"/></svg>
    fendle@tinymugworks.example
  </p>
</section>

</body>
</html>
```